Marlowen

I'm looking for business cards with the logo I've attached. I don't have an specific idea in mind and open to anything. All the usual info will be involved. Name, position in company, nr, email, address

```html
<!DOCTYPE html>
<html lang="en">
<head>
<meta charset="utf-8">
<title>Marlowen Designs – Business Cards</title>
<link href="https://fonts.googleapis.com/css2?family=Montserrat:wght@600;700&family=Poppins:wght@400;500&display=swap" rel="stylesheet">
<style>
  :root{
    --backdrop:#2a2b2d;
    --card-navy:#172c4a;
    --accent-gold:#f0aa27;
    --text-white:#ffffff;
  }
  *{box-sizing:border-box;margin:0;padding:0}
  html,body{width:1200px;height:900px;overflow:hidden}
  body{background:var(--backdrop);position:relative;font-family:"Poppins",sans-serif}
  .card{
    position:absolute;left:276px;width:648px;height:370px;
    background:var(--card-navy);border-radius:26px;
    box-shadow:0 14px 30px rgba(0,0,0,.45);
  }
  .card--front{top:50px}
  .card--back{top:475px}
  .brand{
    font-family:"Montserrat",sans-serif;font-weight:700;color:var(--accent-gold);
    text-transform:uppercase;line-height:1;display:flex;align-items:center;gap:12px;
  }
  .card--front .brand{
    position:absolute;left:0;right:0;top:0;bottom:0;justify-content:center;font-size:40px;letter-spacing:1px;
  }
  .brand-dot{width:16px;height:16px;border-radius:50%;background:var(--accent-gold);flex:none}
  .card--back .brand{position:absolute;left:48px;top:56px;font-size:32px;letter-spacing:1px}
  .card--back .brand-dot{width:13px;height:13px}
  .person{position:absolute;left:48px;top:156px}
  .person-name{font-family:"Montserrat",sans-serif;font-weight:700;font-size:27px;color:var(--text-white);letter-spacing:1.5px;text-transform:uppercase}
  .person-role{font-family:"Montserrat",sans-serif;font-weight:600;font-size:17px;color:var(--accent-gold);letter-spacing:1px;margin-top:4px;text-transform:uppercase}
  .contact-list{position:absolute;left:48px;top:245px;list-style:none}
  .contact-item{display:flex;align-items:center;gap:14px;font-size:17px;color:var(--text-white);height:32px;letter-spacing:.5px}
  .contact-icon{width:20px;height:20px;flex:none}
</style>
</head>
<body>

<section class="card card--front" aria-label="Card front">
  <div class="brand"><span class="brand-dot"></span>Marlowen Designs</div>
</section>

<section class="card card--back" aria-label="Card back">
  <div class="brand"><span class="brand-dot"></span>Marlowen Designs</div>

  <div class="person">
    <p class="person-name">Daniel Okafor</p>
    <p class="person-role">CEO/Founder</p>
  </div>

  <ul class="contact-list">
    <li class="contact-item">
      <svg class="contact-icon" viewBox="0 0 24 24" aria-hidden="true"><path fill="var(--accent-gold)" d="M6.6 10.8a15.1 15.1 0 0 0 6.6 6.6l2.2-2.2a1 1 0 0 1 1-.25 11.4 11.4 0 0 0 3.6.57 1 1 0 0 1 1 1V20a1 1 0 0 1-1 1A17 17 0 0 1 3 4a1 1 0 0 1 1-1h3.5a1 1 0 0 1 1 1c0 1.25.2 2.46.57 3.6a1 1 0 0 1-.25 1z"/></svg>
      214-555-0183
    </li>
    <li class="contact-item">
      <svg class="contact-icon" viewBox="0 0 24 24" aria-hidden="true"><rect x="2" y="5" width="20" height="14" rx="1.5" fill="var(--accent-gold)"/><path d="M3 6.5l9 6.5 9-6.5" stroke="var(--card-navy)" stroke-width="1.6" fill="none"/></svg>
      daniel@marlowenmail.com
    </li>
    <li class="contact-item">
      <svg class="contact-icon" viewBox="0 0 24 24" aria-hidden="true"><path fill="var(--accent-gold)" d="M12 2a7 7 0 0 0-7 7c0 5.2 7 13 7 13s7-7.8 7-13a7 7 0 0 0-7-7zm0 9.5A2.5 2.5 0 1 1 12 6.5a2.5 2.5 0 0 1 0 5z"/></svg>
      418 Harbor Street NE, Suite 210, Alder Falls
    </li>
  </ul>
</section>

</body>
</html>
```